Business Advisory Cards in canvas model

I need a business card to start as an individual advising in business since I am "Bachelor in Business Creation and business innovation" I would like the "Canvas Model" (basic tool to land a business) to represent a part of the logo because it is the simplest and useful model to start, I will advise on business innovation and business creation. Detail: it can be formal, dynamic, colorful, that draws attention, adapted to the millenians.

Target Market(s)

People who want to create their own company. People seeking advice on: negotiation, innovation in business, desing thingking, business creation, coaching in organizational operations, business plan and canvas model.

Contact Information for Business Card

Puede ser colorida pero formal para negociar, que se vea moderna adaptada a los millenians, que se enfoque en “el modelo canvas”.
Que ocupe toda la tarjeta de ambos lados todo el diseño.

Font styles to use
Sans Serif

Colors

Designer to choose colors to be used in the design.

Requirements
Must have
• Canvas model
Nice to have
• Make it a card that makes the person who receives it want to contact the owner of the card. Make it pleasing to the eye.
Should not have
• Negative images, colors that are lost or damage the eyesight.

```html
<!DOCTYPE html>
<html lang="en">
<head>
<meta charset="utf-8">
<title>Business Advisory Cards – Canvas Model</title>
<link href="https://fonts.googleapis.com/css2?family=Arimo:wght@400;500&family=Lato:wght@400;700;900&display=swap" rel="stylesheet">
<style>
  :root {
    --page-bg: #e9e9ec;
    --card-white: #ffffff;
    --brand-pink: #d9449a;
    --tile-pink: #f3dcec;
    --label-ink: #1a1a1a;
    --text-light: #ffffff;
  }
  * { box-sizing: border-box; margin: 0; padding: 0; }
  html, body {
    width: 1200px; height: 1200px; overflow: hidden;
    background: var(--page-bg);
  }
  .stage {
    width: 1200px; height: 1200px;
    display: flex; flex-direction: column; align-items: center; justify-content: center;
    gap: 44px;
  }
  .card {
    width: 960px; height: 540px;
    background: var(--card-white);
    border-radius: 34px;
    padding: 24px;
    box-shadow: 0 6px 22px rgba(0,0,0,0.12);
  }

  /* Front: business model canvas */
  .canvas-model {
    width: 100%; height: 100%;
    display: grid;
    grid-template-columns: repeat(10, 1fr);
    grid-template-rows: 1fr 1fr 0.85fr;
    gap: 10px;
    border-radius: 30px;
    overflow: hidden;
  }
  .block {
    background: var(--tile-pink);
    position: relative;
    padding: 14px 50px 0 16px;
    font-family: "Arimo", Arial, sans-serif;
    font-weight: 500;
    font-size: 16px;
    line-height: 1.1;
    color: var(--label-ink);
  }
  .block .icon {
    position: absolute; top: 22px; right: 10px;
    width: 34px; height: 34px; border-radius: 50%;
    background: var(--brand-pink);
    display: flex; align-items: center; justify-content: center;
  }
  .block .icon svg { width: 19px; height: 19px; }
  .key-partners { grid-column: 1 / 3; grid-row: 1 / 3; }
  .key-activities { grid-column: 3 / 5; grid-row: 1; }
  .key-resources { grid-column: 3 / 5; grid-row: 2; }
  .value-proposition { grid-column: 5 / 7; grid-row: 1 / 3; }
  .customer-relationships { grid-column: 7 / 9; grid-row: 1; }
  .channels { grid-column: 7 / 9; grid-row: 2; }
  .customer-segments { grid-column: 9 / 11; grid-row: 1 / 3; }
  .cost-structure { grid-column: 1 / 6; grid-row: 3; padding-right: 200px; }
  .cost-structure .icon { right: auto; left: 190px; top: 26px; }
  .revenue-streams { grid-column: 6 / 11; grid-row: 3; padding-left: 50px; padding-top: 16px; }
  .revenue-streams .icon { right: auto; left: 290px; top: 46px; }

  /* Back: contact side */
  .contact-panel {
    width: 100%; height: 100%;
    background: var(--brand-pink);
    border-radius: 40px;
    font-family: "Lato", Helvetica, sans-serif;
    color: var(--text-light);
    display: flex; flex-direction: column; align-items: center;
    text-align: center;
    padding-top: 170px;
  }
  .person { font-size: 36px; font-weight: 900; line-height: 1.15; }
  .person .role { font-weight: 400; font-size: 28px; }
  .contact-line { font-size: 27px; font-weight: 400; line-height: 1.25; }
  .contact-line b { font-weight: 700; }
  .tagline { margin-top: auto; margin-bottom: 40px; font-size: 30px; font-weight: 700; }
</style>
</head>
<body>
<main class="stage">

  <section class="card card-front" aria-label="Business model canvas side">
    <div class="canvas-model">
      <div class="block key-partners">Key<br>Partners
        <span class="icon"><svg viewBox="0 0 24 24" fill="none" stroke="#fff" stroke-width="2.4" stroke-linecap="round"><rect x="3" y="9" width="10" height="6" rx="3" transform="rotate(-40 8 12)"/><rect x="11" y="9" width="10" height="6" rx="3" transform="rotate(-40 16 12)"/></svg></span>
      </div>
      <div class="block key-activities">Key<br>Activities
        <span class="icon"><svg viewBox="0 0 24 24" fill="#fff"><path d="M12 2a7 7 0 0 0-7 7c0 5 7 13 7 13s7-8 7-13a7 7 0 0 0-7-7zm0 9.5A2.5 2.5 0 1 1 12 6.5a2.5 2.5 0 0 1 0 5z"/></svg></span>
      </div>
      <div class="block key-resources">Key<br>Resources
        <span class="icon"><svg viewBox="0 0 24 24" fill="#fff"><path d="M12 2a7 7 0 0 0-4 12.7V17h8v-2.3A7 7 0 0 0 12 2z"/><rect x="9" y="18.5" width="6" height="2.5" rx="1"/></svg></span>
      </div>
      <div class="block value-proposition">Value<br>Proposition
        <span class="icon"><svg viewBox="0 0 24 24" fill="#fff"><path d="M3 12V4h8l10 10-8 8z"/><circle cx="7.5" cy="8.5" r="1.6" fill="#d9449a"/></svg></span>
      </div>
      <div class="block customer-relationships">Customer<br>Relationships
        <span class="icon"><svg viewBox="0 0 24 24" fill="#fff"><path d="M12 21s-8-5.3-8-11a4.5 4.5 0 0 1 8-2.8A4.5 4.5 0 0 1 20 10c0 5.7-8 11-8 11z"/></svg></span>
      </div>
      <div class="block channels">Channels
        <span class="icon"><svg viewBox="0 0 24 24" fill="#fff"><rect x="2" y="6" width="12" height="10" rx="1"/><path d="M14 9h4l4 4v3h-8z"/><circle cx="6" cy="17.5" r="2" stroke="#d9449a"/><circle cx="17" cy="17.5" r="2" stroke="#d9449a"/></svg></span>
      </div>
      <div class="block customer-segments">Customer<br>Segments
        <span class="icon"><svg viewBox="0 0 24 24" fill="#fff"><circle cx="8" cy="8" r="3.2"/><circle cx="16" cy="8" r="3.2"/><path d="M2 19c0-3.5 2.7-6 6-6s6 2.5 6 6zM12 19c0-3.5 1.7-6 4-6 3.3 0 6 2.5 6 6z"/></svg></span>
      </div>
      <div class="block cost-structure">Cost Structure
        <span class="icon"><svg viewBox="0 0 24 24" fill="none" stroke="#fff" stroke-width="2"><rect x="3" y="4" width="18" height="16"/><path d="M6 17v-3M10 17v-6M14 17v-4M18 17V9" /><path d="M6 11l4-3 4 2 4-4"/></svg></span>
      </div>
      <div class="block revenue-streams">Revenue Streams
        <span class="icon"><svg viewBox="0 0 24 24" fill="#fff"><path d="M9 3h6l-2 4h-2zM12 8c4 0 7 5 7 9 0 3-3 4-7 4s-7-1-7-4c0-4 3-9 7-9z"/><text x="12" y="18.5" font-size="8" font-family="Arial, sans-serif" font-weight="700" text-anchor="middle" fill="#d9449a">$</text></svg></span>
      </div>
    </div>
  </section>

  <section class="card card-back" aria-label="Contact side">
    <div class="contact-panel">
      <p class="person">Marco Reyes <span class="role">| Owner</span></p>
      <p class="contact-line"><b>P:</b> 555.013.2468 | <b>E:</b> hello@reyesadvise.com</p>
      <p class="contact-line">PO BOX 2040 Elm St, Bristol UK</p>
      <p class="tagline">Bachelor in Business Creation and business innovation</p>
    </div>
  </section>

</main>
</body>
</html>
```